LASIK low price tagline project

Seeking a creative person to create a catchy tag line, with art, for our LASIK laser vision correction pricing. We wish to lowering our price by half, and keep it that low. The tag line I came up with myself is "Great LASIK value. Low LASIK Price". But it's not too catchy. Also, please know it's illegal to imply surgical results; so, we cannot say something like Great LASIK Outcome at a Low LASIK Price. This campaign would be used in our newsletters and as an online campaign. Our brand standards are attached.

Target Market(s)

Creative designers, wordsmiths, marketing mavens

Industry/Entity Type

Health And Wellness

Font styles to use
Sans Serif

Requirements
Must have
• Short catchy tag line
Nice to have
• illiteration or catchy, memorable phrase
Should not have
• Cannot guarantee a surgical result. Cannot imply a surgical result.

```html
<!DOCTYPE html>
<html lang="en">
<head>
<meta charset="utf-8">
<title>LASIK costs now cut by half</title>
<link rel="stylesheet" href="https://fonts.googleapis.com/css2?family=Anton&display=swap">
<style>
  :root {
    --paper: #ffffff;
    --ink: #000000;
    --brand-red: #bc1622;
    --strike-red: #c8283a;
    --old-grey: #a5a8aa;
  }
  html, body {
    margin: 0;
    padding: 0;
    overflow: hidden;
    background: var(--paper);
  }
  .poster {
    position: relative;
    width: 853px;
    height: 1200px;
    overflow: hidden;
    background: var(--paper);
  }
  .poster-art {
    display: block;
    width: 853px;
    height: 1200px;
  }
  .poster-art text {
    font-family: "Anton", "Impact", sans-serif;
    font-weight: 400;
  }
  .old-price { fill: var(--old-grey); }
  .strike { fill: var(--strike-red); opacity: 0.9; }
  .headline { fill: var(--ink); }
  .new-price { fill: var(--brand-red); }
  .offer-band { fill: var(--ink); }
  .offer-text { fill: var(--paper); }
  .brand-mark { fill: var(--brand-red); }
  .brand-name { fill: var(--brand-red); }
</style>
</head>
<body>
<main class="poster">
  <svg class="poster-art" viewBox="0 0 853 1200" role="img" aria-label="Was 100 percent, now 50 percent. We’ve made a correction so you can too. LASIK costs now cut by half. Clearview Vision Center.">
    <g class="was">
      <text class="old-price" x="78" y="207" font-size="174" textLength="393" lengthAdjust="spacingAndGlyphs">100%</text>
      <polygon class="strike" points="58,190 140,160 260,125 380,92 500,62 502,70 385,103 265,137 145,172 60,198"/>
    </g>

    <text class="headline" x="83" y="318" font-size="61" textLength="669" lengthAdjust="spacingAndGlyphs">We’ve made a correction</text>
    <text class="headline" x="84" y="406" font-size="61" textLength="387" lengthAdjust="spacingAndGlyphs">So you can too</text>

    <text class="new-price" x="87" y="790" font-size="378" textLength="674" lengthAdjust="spacingAndGlyphs">50%</text>

    <rect class="offer-band" x="59" y="868" width="734" height="104"/>
    <text class="offer-text" x="74" y="942" font-size="59" textLength="708" lengthAdjust="spacingAndGlyphs">LASIK costs now cut by half</text>

    <g class="brand">
      <rect class="brand-mark" x="63" y="993" width="154" height="154" rx="10"/>
      <text class="brand-name" x="232" y="1101" font-size="74" textLength="561" lengthAdjust="spacingAndGlyphs">Clearview Vision Center</text>
    </g>
  </svg>
</main>
</body>
</html>
```